Business card for acupunctist in Melbourne. Specialises in Fertility, pre and post natal care, pain

I am looking for a business card which is going to catch people eyes. Two sided, one side in a muted colour (keeping it feminine) (pink or yellow???)maybe with a little simple logo or picture, the other side I was thinking white with 3 colours (pink grey and yellow... Had these in mind.
Info on the card
Maren Quillby Acupuncture

Dr Maren Quillby (TCM Acupuncture)
Acupuncture for balancing body and mind.
Verdant Osprey Clinic
14 Corran Lane, Eastwood 3071.
96274158
0438215074
Marentcm@quorvenmail.com

Some other little logo/ designs I have liked are as follows:
http://www.tessrolfeclinic.com/rates-and-insurance/
http://www.corabethwinslow.com/
http://www.zd-needlework.co.uk/

Target Market(s)

professional women, people in pain, active people, people seeking a healthy lifefstyle.

Industry/Entity Type

Business

Font styles to use
Serif
Sans Serif

Colors
eea4c8
fde08a
aaaaaa

Requirements
Must have
• Must be eye catching, but not too loud and busy. Subltle is good. Simple is also good. The logo could be something that represents growth and health and nurturing. Again not too elaborate, very simple.
Thankyou
Should not have
• Electric colours, crazy fonts, Pictures of yin and yang, candles, or bodies.

```html
<!DOCTYPE html>
<html lang="en">
<head>
<meta charset="utf-8">
<title>Maren Quillby Acupuncture – Business Card</title>
<link rel="stylesheet" href="https://fonts.googleapis.com/css2?family=Arimo:wght@400;700&display=swap">
<style>
  :root {
    --card-red: #cc0a00;
    --divider-white: #ffffff;
    --sun-yellow: #fbe36f;
    --stone-grey: #a6b5b4;
    --blossom-pink: #ee5ee6;
    --soft-pink: #f5a3e8;
    --text-white: #ffffff;
    --page: #ffffff;
  }
  * { margin: 0; padding: 0; box-sizing: border-box; }
  html, body {
    width: 1025px; height: 1200px; overflow: hidden;
    background: var(--page);
    font-family: "Arimo", Arial, sans-serif;
  }
  .canvas { position: relative; width: 1025px; height: 1200px; }

  /* Front side */
  .card-front {
    position: absolute; left: 0; top: 0; width: 1025px; height: 585px;
    background: var(--card-red);
  }
  .front-divider { position: absolute; background: var(--divider-white); }
  .front-divider--vertical { left: 859px; top: 0; width: 6px; height: 585px; }
  .front-divider--horizontal { left: 0; top: 454px; width: 1025px; height: 6px; }

  .brand-mark {
    position: absolute; left: 448px; top: 95px;
    width: 84px; height: 84px; border-radius: 50%;
    background: var(--soft-pink);
  }
  .brand-name {
    position: absolute; left: 0; top: 200px; width: 976px;
    text-align: center; color: var(--sun-yellow);
    font-weight: 700; font-size: 70px; line-height: 82px;
    text-transform: uppercase; letter-spacing: 2px;
  }

  /* Back side */
  .card-back {
    position: absolute; left: 0; top: 615px; width: 1025px; height: 585px;
    background: var(--sun-yellow);
  }
  .back-panel { position: absolute; left: 0; top: 0; width: 1025px; height: 585px; }
  .practitioner {
    position: absolute; left: 0; top: 52px; width: 1025px;
    text-align: center; color: var(--blossom-pink);
    font-weight: 700; font-size: 44px; line-height: 52px;
  }
  .contact-details {
    position: absolute; left: 0; top: 225px; width: 1030px;
    text-align: center; color: var(--text-white);
    font-weight: 400; font-size: 38px; line-height: 49px;
    list-style: none;
  }
  .brand-name--small {
    position: absolute; left: 770px; top: 470px; width: 230px;
    text-align: center; color: var(--sun-yellow);
    font-weight: 700; font-size: 24px; line-height: 30px;
    text-transform: uppercase; letter-spacing: 1px;
  }
</style>
</head>
<body>
<main class="canvas">
  <section class="card-front" aria-label="Card front">
    <div class="front-divider front-divider--vertical"></div>
    <div class="front-divider front-divider--horizontal"></div>
    <div class="brand-mark" aria-hidden="true"></div>
    <h1 class="brand-name">Maren Quillby<br>Acupuncture</h1>
  </section>

  <section class="card-back" aria-label="Card back">
    <svg class="back-panel" viewBox="0 0 1025 585" aria-hidden="true">
      <path d="M0,168 Q0,151 16,151 Q512,176 1009,151 Q1025,151 1025,168 L1025,541 L0,541 Z" fill="var(--stone-grey)"/>
    </svg>
    <h2 class="practitioner">Dr Maren Quillby<br>(TCM Acupuncture)</h2>
    <ul class="contact-details">
      <li>Acupuncture for balancing body and mind.</li>
      <li>Verdant Osprey Clinic</li>
      <li>14 Corran Lane, Eastwood 3071.</li>
      <li>96274158</li>
      <li>0438215074</li>
      <li>Marentcm@quorvenmail.com</li>
    </ul>
    <p class="brand-name--small">Maren Quillby<br>Acupuncture</p>
  </section>
</main>
</body>
</html>
```